Hurricane Damage Public Adjuster Billboard

I have created several projects with you and have several great designs. I need to format them into a Billboard for upcoming Hurricane Season. Need done in a month. Im also in process of getting an eye catching and easy to remember 800# Vanity phone number like Call 800-Stormfix or 800- Need Help? My included past Sketch Guild projects will give you an idea of what colors, schemes, and designs I gravitate towards. 3 past Design projects were 1) 2 Logos where I picked the 1st place and the 2nd place and 2) Index Card where I picked the winner as the Index Card and the 2nd place as a Post Card. Point is, I will pick and pay for 2 winners if they're good. This should help to sweeten the pot. Also, please look at my website for ideas that I like:

www.TheClaimWardenGroup.com
I want people to feel that I am the best and highest. Level.

I've been getting a lot of quick half effort designs basically cut & pasting my previous projects. Please don't rush and take your time to be creative. A an example, my Biggest Competitor is Crestline Public Adjusting. Their colors are Black and Gold while mine are Blue, White, and Black with a highlight of Orange if possible. I JUST imported a picture of their BillBoard. I need mine better and BLOW AWAY THEIRS. Terms like "Don't be Victimized Twice ?, Don't let the Hurricane Ruin your Life?". "Get Fairly Paid & Move On" "Our Clients Claims are VIP?
Updates

I'm getting a lot of quick half effort ones. I'd rather you take your time and really put some thoughts and effort into it. My Biggest Competitor is Crestline Public Adjusting. They have black & gold colors, while I have Blue, Black, and white.

It needs to blow theirs away. I have imported their Billboard for comparative purposes.

Guy's,
I'll make it easier for you in what I'm looking for. Please look at the Crestline Billboard picture attached.

1) Put my "Blue Shield" to the left, replacing their logo
2) change color patterns from their (Black, Gold, White) to my color schemes of (Black, Blue, White)
3) I want to see my name where their is:

THE
Claim Warden Group
EXPERT & LOCAL Public Adjusters
"FOR THE POLICYHOLDER!!"

4) to the right, add the A+Rated logo and QTR+ Accredited logo, 5 Star Zentrio Rated logo, 5 Start BLOCKLINK Highly Rated logo, etc..

5) the right side is where you can be creative as I will not have a picture of me there.

"20+ Years of Experience, Recovering Millions for our VIP Clients"

"Your Best, Locally-Based Private Adjuster & Advocate'
"FOR THE POLICYHOLDER!!"

"Don't be victimized Twice!!"

"Don't let the Hurricane Ruin Your Life!!"

This should really help. Also, refer to my website, maybe a couple testimonial fillers?

Thanks all,

marvin@TheClaimWardenGroup.com

Just imported a few awards that would look great to the right side with all the other 5 Star Ratings and accolades.
This right section could be titled like zmy Website:

5 Star Reviews, Ratings & Awards:
4-5 Logos underneath?

Target Market(s)

Coastal place where a Hurricane 🌀 🌀 Hits

Industry/Entity Type

Hurricane Public Insurance Adjuster

Font styles to use
Sans Serif
Other font styles liked:
• Calvera fonts

Colors
0054AA
0677BA
7BADD7
CADEEF
E8F1F8
EE7325
F08F49
F5BC92
FAE3D3
FDF4ED

Requirements
Must have
• Use my past project logos, colors, and schemes to create eye grabbing BillBoard
Nice to have
Should not have
• Not be too busy, must be Easy to Read, Eye Catchy

```html
<!DOCTYPE html>
<html lang="en">
<head>
<meta charset="utf-8">
<title>Claim Warden Group Billboard</title>
<link rel="stylesheet" href="https://fonts.googleapis.com/css2?family=Anton&family=Poppins:ital,wght@0,500;0,600;0,700;1,700&display=swap">
<style>
  :root {
    --navy-deep: #06283f;
    --navy: #0d3e5e;
    --blue: #0677BA;
    --blue-bright: #1a9be0;
    --blue-royal: #0054AA;
    --orange: #EE7325;
    --orange-soft: #F08F49;
    --white: #ffffff;
    --red: #e0202a;
    --green: #6cc04a;
    --stage: #b9b9b9;
  }
  * { margin: 0; padding: 0; box-sizing: border-box; }
  html, body { width: 990px; height: 1200px; overflow: hidden; background: var(--stage); }
  body { position: relative; font-family: "Poppins", sans-serif; }

  .billboard {
    position: absolute; left: 30px; top: 464px;
    width: 930px; height: 271px;
    overflow: hidden;
    box-shadow: 0 14px 24px rgba(0,0,0,.3);
    background: var(--white);
  }
  .billboard__bg { position: absolute; inset: 0; }
  .storm-art {
    position: absolute; left: 600px; top: 0; width: 150px; height: 140px;
    background: radial-gradient(ellipse at 50% 40%, rgba(150,130,230,.55), rgba(90,70,170,.15) 55%, transparent 75%);
  }
  .brand-mark {
    position: absolute; left: 26px; top: 62px; width: 126px;
    text-align: center; color: var(--blue-bright);
    font-weight: 700; font-size: 19px; line-height: 1.1; letter-spacing: .5px;
  }
  .text { position: absolute; white-space: nowrap; }
  .headline-lead { left: 168px; top: 22px; font-size: 28px; font-weight: 500; color: var(--white); letter-spacing: .5px; }
  .headline-main { left: 168px; top: 52px; font-family: "Anton", sans-serif; font-size: 41px; line-height: 1.1; color: var(--orange); }
  .company-name { left: 168px; top: 100px; font-size: 26px; font-weight: 700; color: var(--white); letter-spacing: .3px; }
  .tagline { left: 168px; top: 145px; font-size: 27px; font-weight: 700; font-style: italic; color: var(--white); }

  .phone-icon { position: absolute; left: 30px; top: 200px; width: 44px; height: 44px; }
  .phone-number { left: 86px; top: 188px; font-family: "Anton", sans-serif; font-size: 48px; line-height: 1.3; color: var(--orange); }
  .divider { position: absolute; left: 417px; top: 196px; width: 1px; height: 56px; background: #9aa8b4; }
  .award { left: 431px; top: 190px; font-size: 22px; font-weight: 700; color: var(--blue); line-height: 1.2; }

  .ratings { position: absolute; left: 770px; top: 0; width: 130px; text-align: center; }
  .rating-title { margin-top: 30px; font-size: 24px; font-weight: 700; color: var(--red); line-height: 1; }
  .badge { margin: 11px auto 0; width: 114px; height: 42px; border-radius: 6px; background: var(--navy); border: 2px solid #d7e3ee; }
  .badge-caption { margin-top: 2px; font-size: 9px; font-weight: 700; color: var(--navy); }
  .listing-name { margin-top: 4px; font-size: 27px; font-weight: 600; color: var(--blue); line-height: 1.1; }
  .stars { display: block; margin: 1px auto 0; }
  .listing-name--alt { margin-top: 6px; font-size: 24px; color: var(--green); }
</style>
</head>
<body>
  <section class="billboard" aria-label="Claim Warden Group billboard">
    <svg class="billboard__bg" width="930" height="271" viewBox="0 0 930 271">
      <defs>
        <linearGradient id="darkPanel" x1="0" x2="1">
          <stop offset="0" stop-color="#06283f"/>
          <stop offset="1" stop-color="#124a6e"/>
        </linearGradient>
        <linearGradient id="taglineBand" x1="0" x2="1">
          <stop offset="0" stop-color="#0d3e5e"/>
          <stop offset=".6" stop-color="#0677BA"/>
          <stop offset="1" stop-color="#1a9be0"/>
        </linearGradient>
        <linearGradient id="arc" x1="0" y1="0" x2="0" y2="1">
          <stop offset="0" stop-color="#1aa8ee"/>
          <stop offset="1" stop-color="#0054AA"/>
        </linearGradient>
      </defs>
      <rect width="930" height="186" fill="url(#darkPanel)"/>
      <rect x="150" y="139" width="780" height="47" fill="url(#taglineBand)"/>
      <rect y="186" width="930" height="85" fill="#ffffff"/>
      <path d="M 818 0 C 735 35 700 200 800 271 L 930 271 L 930 0 Z" fill="url(#arc)"/>
      <path d="M 830 0 C 750 38 715 200 812 271 L 930 271 L 930 0 Z" fill="#ffffff"/>
    </svg>

    <div class="storm-art" role="img" aria-label="Lightning bolt striking through the storm sky"></div>

    <div class="brand-mark">CLAIM<br>WARDEN</div>

    <p class="text headline-lead">DON'T LET THE</p>
    <h1 class="text headline-main">HURRICANE RUIN YOUR LIFE?</h1>
    <p class="text company-name">THE CLAIM WARDEN GROUP</p>
    <p class="text tagline">EXPERT &amp; LOCAL Public Adjusters</p>

    <svg class="phone-icon" viewBox="0 0 44 44" aria-hidden="true">
      <circle cx="22" cy="22" r="22" fill="#0d3e5e"/>
      <path d="M15 12 l5 0 l2 6 l-3 3 c2 4 4 6 8 8 l3 -3 l6 2 l0 5 c0 1 -1 2 -2 2 c-12 -1 -20 -9 -21 -21 c0 -1 1 -2 2 -2 z" fill="#ffffff"/>
      <path d="M26 11 a8 8 0 0 1 7 7 M26 6 a13 13 0 0 1 12 12" stroke="#ffffff" stroke-width="2" fill="none" stroke-linecap="round"/>
    </svg>
    <p class="text phone-number">855-STORM AID</p>
    <span class="divider"></span>
    <p class="text award">Voted 2022 BEST Local<br>Public Adjuster</p>

    <aside class="ratings">
      <p class="rating-title">A+ Rating</p>
      <div class="badge"></div>
      <p class="badge-caption">QTR Rating: A+</p>
      <p class="listing-name">Zentrio</p>
      <svg class="stars" width="80" height="15" viewBox="0 0 80 15" aria-label="Five stars">
        <g fill="#f5b400">
          <path id="star" d="M8 0 L10 5 L15.5 5.4 L11.3 8.9 L12.7 14.3 L8 11.3 L3.3 14.3 L4.7 8.9 L0.5 5.4 L6 5 Z"/>
          <use href="#star" x="16"/><use href="#star" x="32"/><use href="#star" x="48"/><use href="#star" x="64"/>
        </g>
      </svg>
      <p class="listing-name listing-name--alt">blocklink</p>
    </aside>
  </section>
</body>
</html>
```